Carvo Group Business Card

Building Management company based in Sydney, Australia. We provide onsite management for commercial and residential buildings.
I would like a sophisticated minimalist design that indicates that we provide a high-end service. I would like a silver or metal look background or something similar.
The business card should have:
Name
Title
email
Office Phone
Mobile
Address
Website
The services that we provide should be prominent:
Building Management - Concierge - Caretaking - Cleaning

```html
<!DOCTYPE html>
<html lang="en">
<head>
<meta charset="utf-8">
<title>Carvo Group Business Card</title>
<link rel="stylesheet" href="https://fonts.googleapis.com/css2?family=Open+Sans:wght@400;600;700&display=swap">
<style>
  :root {
    --backdrop: #2a2a2c;
    --card-black: #141416;
    --card-black-soft: #26272a;
    --brand-blue: #2f6fc1;
    --silver: #c7cacf;
    --text-light: #d6d8db;
    --text-muted: #9a9ca0;
    --ink: #1b1c1f;
    --paper: #ffffff;
  }
  * { box-sizing: border-box; margin: 0; padding: 0; }
  html, body {
    width: 1200px; height: 852px; overflow: hidden;
    background: var(--backdrop);
    font-family: "Open Sans", Arial, sans-serif;
  }
  .canvas {
    position: relative; width: 1200px; height: 852px;
    display: flex; align-items: center; justify-content: center; gap: 40px;
  }
  .card {
    position: relative; width: 540px; height: 310px;
    border-radius: 22px; overflow: hidden;
    box-shadow: 0 18px 40px rgba(0,0,0,.45);
  }

  /* Front */
  .card-front {
    background: radial-gradient(ellipse at 55% 35%, var(--card-black-soft), var(--card-black) 70%);
  }
  .front-brand {
    position: absolute; left: 0; right: 0; top: 104px;
    display: flex; align-items: center; justify-content: center; gap: 14px;
  }
  .brand-mark { width: 18px; height: 18px; background: var(--brand-blue); flex: none; }
  .front-brand .brand-name {
    font-weight: 700; font-size: 40px; letter-spacing: 1px; line-height: 1;
    color: var(--silver);
  }
  .front-web {
    position: absolute; left: 0; right: 0; top: 190px;
    text-align: center; font-size: 15px; letter-spacing: 4px; color: var(--text-light);
  }
  .accent-line { position: absolute; height: 3px; width: 60px; background: var(--brand-blue); }
  .accent-line.right { right: 96px; top: 176px; }
  .accent-line.left  { left: 96px;  top: 226px; }
  .front-services {
    position: absolute; left: 0; right: 0; top: 256px;
    text-align: center; font-size: 11px; letter-spacing: 1.5px;
    text-transform: uppercase; color: var(--text-muted);
  }
  .front-services .sep { color: var(--brand-blue); margin: 0 6px; }

  /* Back */
  .card-back { background: var(--card-black); }
  .back-shapes { position: absolute; inset: 0; }
  .back-brand {
    position: absolute; left: 24px; top: 162px;
    display: flex; align-items: center; gap: 9px;
  }
  .back-brand .brand-name {
    font-weight: 700; font-size: 22px; letter-spacing: .3px; line-height: 1;
    color: var(--ink); white-space: nowrap;
  }
  .back-brand .brand-mark { width: 13px; height: 13px; }
  .contact { position: absolute; left: 292px; top: 44px; color: var(--text-light); }
  .contact-name { font-weight: 700; font-size: 19px; color: var(--brand-blue); }
  .contact-title { font-size: 12px; color: var(--text-muted); margin-top: 2px; }
  .contact-list { list-style: none; margin-top: 34px; }
  .contact-list li {
    display: flex; align-items: center; gap: 10px;
    font-size: 12.5px; line-height: 18px; white-space: nowrap;
  }
  .contact-list svg { width: 12px; height: 12px; fill: var(--brand-blue); flex: none; }
  .contact-address { font-size: 12.5px; line-height: 18px; margin-top: 14px; padding-left: 22px; white-space: nowrap; }
</style>
</head>
<body>
<main class="canvas">

  <section class="card card-front" aria-label="Business card front">
    <div class="front-brand">
      <span class="brand-mark"></span>
      <span class="brand-name">CARVO GROUP</span>
    </div>
    <span class="accent-line right"></span>
    <p class="front-web">www.carvogroup.co.uk</p>
    <span class="accent-line left"></span>
    <p class="front-services">Building Management<span class="sep">|</span>Concierge<span class="sep">|</span>Caretaking<span class="sep">|</span>Cleaning</p>
  </section>

  <section class="card card-back" aria-label="Business card back">
    <svg class="back-shapes" viewBox="0 0 540 310" preserveAspectRatio="none">
      <path d="M0 -10 C 180 0 300 140 250 320 L0 320 Z" fill="#2f6fc1"/>
      <path d="M0 0 C 170 10 285 140 238 320 L0 320 Z" fill="#ffffff"/>
    </svg>
    <div class="back-brand">
      <span class="brand-mark"></span>
      <span class="brand-name">CARVO GROUP</span>
    </div>
    <div class="contact">
      <p class="contact-name">Your Long Name</p>
      <p class="contact-title">Managing Director</p>
      <ul class="contact-list">
        <li><svg viewBox="0 0 12 12"><path d="M2 1h2.5l1 3-1.5 1a7 7 0 0 0 3 3l1-1.5 3 1V11C5 11 1 7 1 2z"/></svg>00.00.00.0000</li>
        <li><svg viewBox="0 0 12 12"><rect x="3" y="0.5" width="6" height="11" rx="1"/></svg>00.00.00.0000</li>
        <li><svg viewBox="0 0 12 12"><path d="M0 2h12v8H0z M0 2l6 4 6-4"/></svg>yourname@yourwebsite.com</li>
        <li><svg viewBox="0 0 12 12"><circle cx="6" cy="6" r="5.5"/></svg>www.yourwebsite.com</li>
      </ul>
      <p class="contact-address">Your Commercial or office address<br>in just two line with pincode</p>
    </div>
  </section>

</main>
</body>
</html>
```